Consultant company (start up) needs a bold, yet simple web design

We need a we design for "Kestrel Analys & Rådgivning". As our name implies we are a consultant firm helping companies with public sector business (tenders), but also helping the buyer side. We provide market research and reports, advice (legal and business) and hands-on-help with tender applications (projectleader; analysing critiera and texts, document reviews, etc). We have a rather uniqe position in our market with our mixed competences of branding and market communication, formal management systems, and public tenders.

We have a strong drive to make tender business simple for our clients: we will take care of the complicated!

We want our web design to be bold, yet clean and simple, communicating:

Competence; Commitment, Simplicity (for the customer).
Updates

Reason: For different reasons our web project was put on hold/was delayed a few days. As of today we are kicking life into it again, and expect to come back with feedback on designs in the next days. Best regards, Henrik

Target Market(s)

We primarily help companies aiming for public contracts.

Industry/Entity Type

Business Consultant

Contact Information for Business Card

Company logo; First name, Last name, Titel, webadress; personal e-mail
Maybe: a motto like "Offentliga affärer. Enklare" ("Public business. Made simple.")

Coding

Coded - Design and coding required

Font styles to use
Sans Serif

Colors

Designer to choose colors to be used in the design.

Requirements
Must have
• Dual language (Swedish and English)
• Responsive design, many people will view our webpage on their phone or ipad.
• We want to make our position clear, stating what distinguishes us from "the rest of the pack" in maybe with on the starting page.
• [Will update brief; need to think this through]
Nice to have
• We have our logo in three colours. Green is our first. We are not yet sure why we have the different colurs. Maybe (just maybe!) the different colours can be put to use?
• We need help with the choice of images.
Should not have
• Never boring.

```html
<!DOCTYPE html>
<html lang="en">
<head>
<meta charset="utf-8">
<title>Kestrel Analys &amp; Rådgivning</title>
<link rel="stylesheet" href="https://fonts.googleapis.com/css2?family=Raleway:wght@400;500;600&family=Lato:ital,wght@0,400;0,700;1,400&display=swap">
<style>
:root{
  --green:#8cbb3c;
  --green-dark:#2f7d3a;
  --ink:#222;
  --text:#444;
  --muted:#666;
  --topbar:#5b5b5b;
  --light:#f1f1f1;
  --footer:#333333;
  --line:#dcdcdc;
  --white:#fff;
}
*{box-sizing:border-box;margin:0;padding:0}
html,body{width:670px;height:1200px;overflow:hidden;background:var(--white)}
body{position:relative;font-family:"Lato",sans-serif;color:var(--text)}
.abs{position:absolute}
.heading{font-family:"Raleway",sans-serif;font-weight:400;color:var(--ink)}
.heading em{font-style:normal;color:var(--green)}

/* top bar & header */
.topbar{left:0;top:0;width:670px;height:21px;background:var(--topbar);color:var(--white);font-size:8px}
.topbar .contact{position:absolute;top:6px;display:flex;align-items:center;gap:4px}
.flag{position:absolute;left:557px;top:6px;width:14px;height:9px;background:#2a3f8f;border:1px solid #fff}
.flag::before{content:"";position:absolute;left:5px;top:0;width:2px;height:7px;background:#d22}
.flag::after{content:"";position:absolute;left:0;top:3px;width:12px;height:2px;background:#d22}
.caret{position:absolute;left:574px;top:9px;border:3px solid transparent;border-top-color:#fff}
.header{left:0;top:21px;width:670px;height:51px;background:var(--white)}
.logo-tab{left:92px;top:8px;width:176px;height:64px;background:var(--white);border-radius:6px 6px 0 0;display:flex;align-items:center;gap:8px;padding-left:14px}
.logo-dot{width:26px;height:26px;border-radius:50%;background:var(--green);flex:none}
.logo-name{font-family:"Raleway",sans-serif;font-weight:500;font-size:13px;line-height:15px;color:#555}
.nav{top:42px;font-family:"Raleway",sans-serif;font-size:8px;color:#333}
.nav.active{color:var(--green-dark)}
.nav-sep{top:44px;width:1px;height:6px;background:#ccc}

/* hero */
.hero{left:0;top:72px;width:670px;height:293px;background:radial-gradient(ellipse at 72% 45%,#8a98a8 0%,#5c6d80 40%,#34475c 100%)}
.hero-title{left:91px;top:188px;font-family:"Raleway",sans-serif;font-size:14.5px;color:var(--white);letter-spacing:.2px}
.hero-sub{left:91px;top:212px;font-size:7.4px;line-height:11px;color:var(--white)}
.btn{display:flex;align-items:center;justify-content:space-between;height:18px;border-radius:9px;padding:0 3px 0 6px;font-family:"Lato",sans-serif;font-weight:700;font-size:6.8px;color:var(--white);background:var(--green)}
.btn .arrow{width:12px;height:12px;border-radius:50%;background:var(--white);display:flex;align-items:center;justify-content:center}
.dots{display:flex;gap:3.5px}
.dots span{width:5.5px;height:5.5px;border-radius:50%;border:1px solid #fff}
.dots span.on{background:var(--green);border-color:var(--green)}
.dots.dark span{border-color:#666}
.dots.dark span.on{border-color:var(--green)}

/* about */
.about-title{left:90px;top:389px;font-size:15px}
.rule{height:1px;background:var(--line)}
.rule-accent{height:2px;background:var(--green)}
.about-lead{left:90px;top:426px;width:310px;font-size:6.4px;line-height:10.5px;font-weight:700;color:var(--ink)}
.about-body{left:90px;top:453px;width:310px;font-size:6.3px;line-height:11.3px;color:var(--muted)}

.inquiry{left:438px;top:392px;width:142px;height:150px;background:var(--white);box-shadow:0 3px 6px rgba(0,0,0,.2)}
.inquiry-head{height:25px;background:var(--green);color:var(--white);font-family:"Raleway",sans-serif;font-size:12px;display:flex;align-items:center;justify-content:center}
.field{position:absolute;left:8px;width:126px;height:18px;border:1px solid #ddd;font-size:6px;color:#777;padding:5px 5px}
.field i{font-style:normal;color:#c33}

/* services */
.services{left:0;top:576px;width:670px;height:286px;background:var(--light)}
.section-title{width:670px;text-align:center;font-size:15px}
.card{top:636px;width:155px;height:94px;background:var(--white);border:1px solid #ddd;padding:3px}
.card.active{border-color:var(--green)}
.card-img{width:100%;height:100%}
.card-shadow{top:730px;width:135px;height:6px;border-radius:50%;background:radial-gradient(ellipse,rgba(0,0,0,.35),transparent 70%)}
.svc-title{top:740px;width:155px;text-align:center;font-family:"Raleway",sans-serif;font-size:9.3px;line-height:11px;color:var(--ink)}
.svc-title.active{color:var(--green)}
.svc-text{top:768px;width:155px;text-align:center;font-size:6.3px;line-height:8.8px;color:#333}
.plus{top:803px;width:15px;height:15px;border-radius:50%;background:#999}
.plus.active{background:var(--green)}

/* testimonials */
.portrait{left:170px;top:922px;width:80px;height:80px;border-radius:50%;border:3px solid #eee;background:radial-gradient(circle at 50% 40%,#d9d9d9,#a9a9a9)}
.quote-text{left:263px;top:920px;width:235px;font-style:italic;font-size:6.5px;line-height:12.5px;color:#333}
.quote-name{left:263px;top:983px;width:228px;text-align:right;font-family:"Raleway",sans-serif;font-size:8.5px;color:var(--green)}
.quote-role{left:263px;top:994px;width:228px;text-align:right;font-size:5.8px;color:#333}

/* footer */
.footer{left:0;top:1030px;width:670px;height:148px;background:var(--footer)}
.foot-head{top:1054px;font-family:"Raleway",sans-serif;font-size:10px;color:var(--white)}
.foot-rule{top:1073px;height:1px;background:#555}
.foot-link{left:91px;font-size:6.3px;color:#bbb}
.foot-link.active{color:var(--green)}
.foot-link::before{content:"›";color:#888;margin-right:4px}
.foot-div{top:1054px;width:1px;height:98px;background:#444}
.foot-text{font-size:6.3px;color:#bbb;line-height:9px}
.map{left:322px;top:1082px;width:131px;height:70px;background:linear-gradient(135deg,#d8dccf,#c9cfbe 60%,#e6d98f)}
.foot-logo{left:483px;top:1086px;display:flex;align-items:center;gap:6px}
.foot-logo .logo-dot{width:18px;height:18px;background:#999}
.foot-logo .logo-name{font-size:9px;line-height:10px;color:#aaa}
.social{top:1119px;width:14px;height:14px;border-radius:50%}
.copyright{left:0;top:1178px;width:670px;height:22px;background:var(--green);color:var(--white);font-size:6.3px;display:flex;align-items:center;justify-content:center}
</style>
</head>
<body>

<!-- top bar -->
<div class="abs topbar">
  <div class="contact" style="left:396px">
    <svg width="9" height="8" viewBox="0 0 9 8"><path d="M1 3.5 4.5 1 8 3.5V7H1Z" fill="none" stroke="#fff" stroke-width="1"/></svg>
    info@kestrelanalys.se
  </div>
  <div class="contact" style="left:484px">
    <svg width="12" height="12" viewBox="0 0 12 12"><circle cx="6" cy="6" r="5.3" fill="none" stroke="#fff" stroke-width=".9"/><path d="M4 3.3c.5-.3.8 0 1 .6l.2.6c.1.3-.3.6-.4.8.3.7.9 1.3 1.5 1.6.2-.2.4-.6.8-.4l.6.3c.5.2.7.6.4 1-.6.7-1.7.5-2.7-.3C4.3 6.5 3.6 5.3 3.7 4c0-.3.1-.5.3-.7Z" fill="#fff"/></svg>
    070-555-0148
  </div>
  <div class="flag"></div>
  <div class="caret"></div>
</div>

<div class="abs header"></div>
<div class="abs logo-tab">
  <span class="logo-dot"></span>
  <span class="logo-name">Kestrel Analys<br>&amp; Rådgivning</span>
</div>

<span class="abs nav active" style="left:311px">Home</span>
<span class="abs nav-sep" style="left:356px"></span>
<span class="abs nav" style="left:380px">About Us</span>
<span class="abs nav-sep" style="left:437px"></span>
<span class="abs nav" style="left:460px">Services</span>
<span class="abs nav-sep" style="left:515px"></span>
<span class="abs nav" style="left:539px">Contact Us</span>

<!-- hero -->
<div class="abs hero" role="img" aria-label="Photo of a hand placing the last piece into a blue jigsaw puzzle"></div>
<h1 class="abs hero-title" style="font-weight:400">WELCOME TO KESTREL ANALYS</h1>
<p class="abs hero-sub">We Are A Consultant Company That Helps Companies With<br>Public Sector Business But Also Helping The Buyers.</p>
<a class="abs btn" style="left:91px;top:242px;width:66px">READ MORE <span class="arrow"><svg width="6" height="6" viewBox="0 0 6 6"><path d="M2 1 4 3 2 5" fill="none" stroke="#333" stroke-width="1"/></svg></span></a>
<div class="abs dots" style="left:91px;top:270px"><span class="on"></span><span></span><span></span><span></span></div>

<!-- about -->
<h2 class="abs heading about-title">About <em>Us</em></h2>
<div class="abs rule" style="left:90px;top:414px;width:308px"></div>
<div class="abs rule-accent" style="left:90px;top:413px;width:26px"></div>
<p class="abs about-lead">Nemo enim ipsam voluptatem quia voluptas sit aspernatur aut odit aut fugit, sed quia consequuntur magni dolores eos qui ratione voluptatem</p>
<p class="abs about-body">Lorem ipsum dolor sit amet, consectetur adipiscing elit, sed do eiusmod tempor incididunt ut labore et dolore magna aliqua. Ut enim ad minim veniam, quis nostrud exercitation ullamco laboris nisi ut aliquip ex ea commodo consequat. Duis aute irure dolor in reprehenderit in voluptate velit esse cillum dolore eu fugiat nulla pariatur. Excepteur sint occaecat cupidatat non proident, sunt in culpa qui officia deserunt mollit anim id est laborumLorem ipsum dolor sit amet, consectetur adipiscing elit, sed do eiusmod tempor incididunt ut labore et dolore magna aliqua.</p>
<a class="abs btn" style="left:90px;top:533px;width:67px">READ MORE <span class="arrow"><svg width="6" height="6" viewBox="0 0 6 6"><path d="M2 1 4 3 2 5" fill="none" stroke="#333" stroke-width="1"/></svg></span></a>

<form class="abs inquiry">
  <div class="inquiry-head">Quick Inquiry</div>
  <div class="field" style="top:36px">Your Name<i>*</i></div>
  <div class="field" style="top:58px">Your Email<i>*</i></div>
  <div class="field" style="top:79px">Your Phone<i>*</i></div>
  <div class="field" style="top:101px;height:31px">Your Message<i>*</i></div>
</form>
<a class="abs btn" style="left:471px;top:533px;width:76px;background:var(--green-dark)">SUBMIT FORM <span class="arrow"><svg width="6" height="6" viewBox="0 0 6 6"><path d="M2 1 4 3 2 5" fill="none" stroke="#333" stroke-width="1"/></svg></span></a>

<!-- services -->
<div class="abs services"></div>
<h2 class="abs heading section-title" style="left:0;top:600px">Our <em>Services</em></h2>
<div class="abs rule" style="left:258px;top:622px;width:154px;background:#ccc"></div>
<div class="abs rule-accent" style="left:322px;top:621px;width:26px"></div>

<div class="abs card active" style="left:90px"><div class="card-img" role="img" aria-label="Photo of a hand touching a tablet showing market charts" style="background:linear-gradient(135deg,#e6eef6,#9fb6cf 60%,#5f7f9f)"></div></div>
<div class="abs card" style="left:258px"><div class="card-img" role="img" aria-label="Photo of business people meeting around a table" style="background:linear-gradient(135deg,#e9edf2,#b8c2cc 55%,#3a4450)"></div></div>
<div class="abs card" style="left:426px"><div class="card-img" role="img" aria-label="Photo of a consultant reading a document folder" style="background:linear-gradient(135deg,#dfe8e2,#b9c4bf 50%,#eef0ee)"></div></div>
<div class="abs card-shadow" style="left:100px"></div>
<div class="abs card-shadow" style="left:268px"></div>
<div class="abs card-shadow" style="left:436px"></div>

<h3 class="abs svc-title active" style="left:90px;font-weight:400">Market Research And<br>Reports</h3>
<h3 class="abs svc-title" style="left:258px;font-weight:400">Advice Legal And<br>Business</h3>
<h3 class="abs svc-title" style="left:426px;font-weight:400">Hands-on-help With Tender<br>Applications</h3>
<p class="abs svc-text" style="left:90px">Lorem ipsum dolor sit amet, consectetuer adipiscing elit, sed diam nonummy nibh euismod tincidunt ut laoreet dolore.</p>
<p class="abs svc-text" style="left:258px">Lorem ipsum dolor sit amet, consectetuer adipiscing elit, sed diam nonummy nibh euismod tincidunt ut laoreet dolore.</p>
<p class="abs svc-text" style="left:426px">Lorem ipsum dolor sit amet, consectetuer adipiscing elit, sed diam nonummy nibh euismod tincidunt ut laoreet dolore.</p>

<svg class="abs plus active" style="left:160px" viewBox="0 0 15 15"><path d="M7.5 3.5v8M3.5 7.5h8" stroke="#fff" stroke-width="2.2"/></svg>
<svg class="abs plus" style="left:328px" viewBox="0 0 15 15"><path d="M7.5 3.5v8M3.5 7.5h8" stroke="#fff" stroke-width="2.2"/></svg>
<svg class="abs plus" style="left:495px" viewBox="0 0 15 15"><path d="M7.5 3.5v8M3.5 7.5h8" stroke="#fff" stroke-width="2.2"/></svg>
<div class="abs dots dark" style="left:318px;top:832px"><span class="on"></span><span></span><span></span><span></span></div>

<!-- testimonials -->
<h2 class="abs heading section-title" style="left:0;top:886px">Clients <em>Testimonials</em></h2>
<div class="abs rule" style="left:258px;top:908px;width:154px"></div>
<div class="abs rule-accent" style="left:322px;top:907px;width:26px"></div>

<svg class="abs" style="left:64px;top:958px" width="16" height="26" viewBox="0 0 16 26"><path d="M13 2 3 13l10 11" fill="none" stroke="#ccc" stroke-width="1.2"/></svg>
<svg class="abs" style="left:590px;top:958px" width="16" height="26" viewBox="0 0 16 26"><path d="M3 2l10 11L3 24" fill="none" stroke="#ccc" stroke-width="1.2"/></svg>
<svg class="abs" style="left:118px;top:940px" width="36" height="29" viewBox="0 0 36 29"><g fill="#ddd"><path d="M0 0h14v14H9v15H0Z"/><path d="M20 0h14v14h-5v15h-9Z"/></g></svg>
<svg class="abs" style="left:516px;top:940px" width="36" height="29" viewBox="0 0 36 29"><g fill="#ddd"><path d="M16 29H2V15h5V0h9Z"/><path d="M36 29H22V15h5V0h9Z"/></g></svg>

<div class="abs portrait" role="img" aria-label="Portrait photo of the client giving the testimonial"></div>
<p class="abs quote-text">Lorem ipsum dolor sit amet, consectetuer adipiscing elit, sed diam nonummy nibh euismod tincidunt ut laoreet dolore magna aliquam erat volutpat. Ut wisi enim ad minim veniam, quis nostrud exer tation ullamcorper suscipit loboutlaoreet Duissed diam nonummyconsequat. Duissed diam nonummy nibh euismod tincidunt ut laoreet dolore magna .</p>
<p class="abs quote-name">- Marcus Lindqvist</p>
<p class="abs quote-role">CEO &amp; FOUNDER</p>

<!-- footer -->
<footer class="abs footer"></footer>
<h4 class="abs foot-head" style="left:91px;font-weight:400">Quick Links</h4>
<div class="abs foot-rule" style="left:91px;width:56px"></div>
<a class="abs foot-link active" style="top:1083px">Home</a>
<a class="abs foot-link" style="top:1100px">About Us</a>
<a class="abs foot-link" style="top:1118px">Services</a>
<a class="abs foot-link" style="top:1136px">Contact Us</a>
<div class="abs foot-div" style="left:165px"></div>

<h4 class="abs foot-head" style="left:178px;font-weight:400">Contact Detail</h4>
<div class="abs foot-rule" style="left:178px;width:110px"></div>
<p class="abs foot-text" style="left:178px;top:1082px;color:#fff;font-size:7px">Kestrel Analys</p>
<p class="abs foot-text" style="left:178px;top:1094px;width:115px">Lorem ipsum dolor sit amet, consecte adipiscing elit,</p>
<svg class="abs" style="left:178px;top:1124px" width="8" height="8" viewBox="0 0 8 8"><path d="M1.5.5c.6-.3 1 0 1.2.6l.3.8c.1.3-.3.7-.5.9.4.8 1 1.4 1.8 1.8.2-.2.6-.6.9-.5l.8.3c.6.2.8.6.5 1.1-.7.8-2 .6-3.2-.4C2 4.3 1.1 2.8 1.2 1.4Z" fill="var(--green)"/></svg>
<p class="abs foot-text" style="left:191px;top:1122px;font-size:8px;color:#ddd">070-555-0148</p>
<svg class="abs" style="left:178px;top:1142px" width="8" height="6" viewBox="0 0 8 6"><rect width="8" height="6" fill="var(--green)"/><path d="M0 0 4 3.2 8 0" fill="none" stroke="#333" stroke-width=".8"/></svg>
<p class="abs foot-text" style="left:191px;top:1140px">info@kestrelanalys.se</p>
<div class="abs foot-div" style="left:305px"></div>

<h4 class="abs foot-head" style="left:322px;font-weight:400">Location Map</h4>
<div class="abs foot-rule" style="left:322px;width:131px"></div>
<div class="abs map" role="img" aria-label="Street map showing the office location"></div>

<div class="abs foot-logo">
  <span class="logo-dot"></span>
  <span class="logo-name">Kestrel Analys<br>&amp; Rådgivning</span>
</div>
<span class="abs social" style="left:497px;background:#3b5998"></span>
<span class="abs social" style="left:515px;background:#1da1f2"></span>
<span class="abs social" style="left:534px;background:#0e76a8"></span>
<span class="abs social" style="left:552px;background:#dd4b39"></span>

<div class="abs copyright">Copyright © 2017 Kestrel Analys . All Rights Reserved.</div>

</body>
</html>
```